Web site for radio show

I've got a radio show starting on VandorFM and need a web site for it. I am familiar with WordPress, so I'd like to get a design for a WordPress-based web site for the show.

I'm also posting a logo project to be done at the same time.

The best radio show web site I've seen is the Lumen Tuesday site (www.lumentuesday.example). That's a good model but I don't want to start with that much complexity and content. The initial site that I'd like you to design would have the following parts:
- Upcoming shows
- Past shows (including links to authors, their web sites, and their books)
- Chirply feed
- Blog
- About
- ...and anything else you think would be necessary

For colors, I'd like it to be consistent with my personal web site: www.haldanecraftworks.example

Target Market(s)

The target market for this show is mid- to upper-level managers

Industry/Entity Type

Radio

Requirements
Must have
• The project has to proceed in (at least) two stages: a first rough layout, and a second finished design. Whether you want a third stage in between with look and feel options is up to you.

```html
<!DOCTYPE html>
<html lang="en">
<head>
<meta charset="utf-8">
<title>Haldane Show</title>
<link rel="stylesheet" href="https://fonts.googleapis.com/css2?family=Nunito+Sans:wght@400;600;700&family=Roboto+Condensed:wght@400;700&display=swap">
<style>
:root{
  --red:#c8171e;
  --ink:#222;
  --body:#444;
  --link:#23305e;
  --panel:#ededed;
  --bar:#e2e2e2;
  --line:#d6d6d6;
  --canvas:#d9d9d9;
  --footer:#3d3d3d;
  --chirp:#2a9fd8;
  --white:#fff;
}
*{box-sizing:border-box;margin:0;padding:0}
html,body{width:814px;height:1200px;overflow:hidden}
body{background:var(--canvas);font-family:"Nunito Sans",Arial,sans-serif;color:var(--body)}
.page{position:absolute;left:116px;top:0;width:582px;height:1200px;background:var(--white)}
.abs{position:absolute}
.topbar{left:0;top:0;width:582px;height:27px;background:#f3f3f3;border-bottom:2px solid var(--red)}
.phone{left:8px;top:8px;font-size:7.5px;color:#333;display:flex;align-items:center;gap:3px}
.social{right:8px;top:4px;display:flex;gap:4px}
.social span{width:18px;height:18px;border-radius:50%;display:block}
.brand{left:8px;top:40px;font-family:"Roboto Condensed",sans-serif;font-weight:700;font-size:25px;color:var(--ink);letter-spacing:-.3px}
.search{left:430px;top:44px;width:145px;height:19px;border:1px solid #bbb;background:#fafafa;font-size:7px;color:#aaa;padding:5px 4px;box-shadow:inset 0 0 0 2px #eee}
.search svg{position:absolute;right:4px;top:5px}
.nav{left:0;top:77px;width:582px;height:30px;border-top:1px solid var(--line);border-bottom:3px solid var(--red);display:flex}
.nav a{height:26px;line-height:27px;font-size:10.5px;color:#333;text-decoration:none;border-right:1px solid var(--line);text-align:center;position:relative}
.nav a.active::after{content:"";position:absolute;left:50%;bottom:-1px;margin-left:-4px;border:4px solid transparent;border-bottom-color:var(--red)}
.hero{left:0;top:108px;width:582px;height:257px;background:linear-gradient(120deg,#3a3330 0%,#6b5a4c 35%,#2a2624 60%,#4a4a4a 100%)}
.hero-cap{left:36px;top:145px;width:296px;height:73px;background:rgba(190,30,25,.78);color:#fff;padding:6px 6px}
.hero-cap h2{font-weight:400;font-size:10px;margin-bottom:4px}
.hero-cap p{font-size:6.3px;line-height:10.3px}
.arrow{width:12px;height:12px;border-radius:50%;background:rgba(230,230,230,.85);top:104px}
.dots{left:265px;top:246px;display:flex;gap:2px;background:rgba(220,220,220,.7);padding:2px 3px;border-radius:3px}
.dots i{width:6px;height:6px;border-radius:50%;background:#999;display:block}
.dots i.on{background:var(--red)}
.h-under{font-size:11px;color:var(--ink);font-weight:400}
.h-under::after{content:"";display:block;height:2px;background:var(--red);margin-top:3px}
.welcome{left:9px;top:378px;width:133px}
.intro{left:11px;top:403px;width:560px;font-size:6.6px;line-height:10.3px;color:#333}
.intro p{margin-bottom:5px}
.panel{left:6px;top:472px;width:571px;height:418px;background:var(--panel);border:1px solid #e2e2e2}
.barhead{height:20px;background:var(--bar);border-bottom:1px dotted #777;display:flex;justify-content:space-between;align-items:center;padding:0 6px}
.barhead h3{font-family:"Roboto Condensed",sans-serif;font-size:11px;font-weight:700;color:#222;letter-spacing:-.3px}
.barhead a{font-size:6.3px;color:var(--red);text-decoration:none}
.photo{background:linear-gradient(135deg,#8a6d4e,#b9a58a 50%,#5c5248)}
.photo.cool{background:linear-gradient(135deg,#2b3c6b,#707a8a 50%,#2a2a2a)}
.photo.room{background:linear-gradient(135deg,#9a9690,#c8c2b8 50%,#4a5a78)}
.photo.warm{background:linear-gradient(135deg,#6b5432,#b89a62 50%,#2c2420)}
.card{width:171px}
.card .photo{height:100px}
.card h4{font-size:7.8px;font-weight:600;color:#222;margin-top:13px}
.card .meta{font-size:7.8px;color:#333;line-height:11.5px;margin-top:1px}
.card .meta .date{font-size:6.6px;color:#555;padding-left:2px}
.card .meta a{color:var(--link);text-decoration:none}
.card .desc{font-size:7.9px;color:#666;line-height:13.8px;margin-top:4px;padding-right:6px}
.card .more{color:var(--red);float:right}
.thumb{width:114px}
.thumb .photo{height:67px}
.thumb p{font-size:5.3px;color:#222;line-height:8.5px;margin-top:5px}
.thumb small{display:block;font-size:4.2px;line-height:6px;color:#666}
.videobox{left:396px;top:285px;width:167px;height:132px;background:#d4d4d4;border:1px solid #c8c8c8;padding:14px 8px}
.videobox .h-under{width:128px}
.videobox .photo{margin:11px 3px 0;height:78px;position:relative}
.col{top:915px}
.list-item{border-bottom:1px dotted #555;padding:6px 0 5px 4px;font-size:6.8px;line-height:13.8px;color:#444}
.list-item .date,.chirp .date{display:block;color:var(--red);font-size:6.8px;line-height:12px}
.chirp{display:flex;gap:6px;padding-top:6px;font-size:6.8px;line-height:13.8px;color:#444;height:51px}
.chirp.first{padding-top:10px;height:55px}
.chirp .dot{width:9px;height:9px;border-radius:50%;background:var(--chirp);flex:none;margin-top:3px}
.playlist{left:392px;top:916px;width:184px;height:214px;border:1px solid #ccc;background:#fff}
.playlist header{background:var(--red);color:#fff;font-size:7.8px;height:23px;line-height:24px;padding-left:8px}
.track{margin:0 6px;border-bottom:1px solid #e0e0e0;padding:7px 1px 3px;font-size:7px;color:#333;height:62px}
.track h5{font-size:6.8px;font-weight:600;color:#222;margin-bottom:4px}
.track p{line-height:14px;padding-right:12px}
.track .play{color:var(--red);float:right;margin-right:-10px}
.more-list{font-size:6.8px;color:var(--red);text-align:right;padding:4px 8px}
.footer{left:0;top:1154px;width:582px;height:46px;background:var(--footer);color:#ccc}
.foot-links{left:18px;top:16px;display:flex;gap:13px;font-size:6.8px}
.copy{left:18px;top:33px;font-size:6px;color:#aaa}
.foot-brand{left:450px;top:12px;display:flex;align-items:center;gap:5px;font-size:15px;font-weight:700;color:var(--chirp)}
.foot-brand .sq{width:10px;height:10px;border-radius:50%;background:var(--chirp)}
</style>
</head>
<body>
<div class="page">
  <div class="abs topbar">
    <div class="abs phone">
      <svg width="12" height="9" viewBox="0 0 12 9"><path d="M1 7c0-3 2-5 4-6l1 2-2 1c0 1 1 2 2 2l1-2 2 1c-1 2-3 3-5 3H1z" fill="#333"/><line x1="0" y1="8.5" x2="12" y2="8.5" stroke="#333"/></svg>
      <span>- 555 010 234</span>
    </div>
    <div class="abs social">
      <span style="background:#3b5aa0" aria-label="Social profile"></span>
      <span style="background:#3fb6ee" aria-label="Chirply profile"></span>
      <span style="background:#1f7bb6" aria-label="Professional profile"></span>
      <span style="background:#e8e8e8;border:1px solid #ccc" aria-label="Photo profile"></span>
    </div>
  </div>

  <div class="abs brand">HALDANE SHOW</div>
  <div class="abs search">Enter Your Search...
    <svg width="8" height="8" viewBox="0 0 8 8"><circle cx="3.2" cy="3.2" r="2.4" fill="none" stroke="#555" stroke-width="1"/><line x1="5" y1="5" x2="7.5" y2="7.5" stroke="#555" stroke-width="1.2"/></svg>
  </div>

  <nav class="abs nav">
    <a class="active" style="width:60px">HOME</a>
    <a style="width:59px">ABOUT</a>
    <a style="width:123px">UPCOMING SHOWS</a>
    <a style="width:93px">PAST SHOWS</a>
    <a style="width:59px">EVENTS</a>
    <a style="width:59px">BLOG</a>
    <a style="width:56px">NEWS</a>
    <a style="width:73px;border-right:0">CONTACT</a>
  </nav>

  <div class="abs hero" role="img" aria-label="Radio studio with microphone and headphones">
    <div class="abs arrow" style="left:8px"><svg width="12" height="12"><path d="M7 3.5 4.5 6 7 8.5" stroke="#333" fill="none" stroke-width="1.3"/></svg></div>
    <div class="abs arrow" style="left:562px"><svg width="12" height="12"><path d="M5 3.5 7.5 6 5 8.5" stroke="#333" fill="none" stroke-width="1.3"/></svg></div>
    <div class="abs hero-cap">
      <h2>Lorem Ipsm Dolor sit amet..</h2>
      <p>Lorem ipsum dolor sit amet, consectetur adipisicing elit, sed do eiusmod tempor incid-idunt ut labore et dolore magna aliqua. Ut enim ad minim veniam.Lorem ipsum dolor sit amet, consectetur adipisicing elit, sed do eiusmod tempor incididunt ut labore et dolore magna aliqua. Ut enim ad minim veniam.</p>
    </div>
    <div class="abs dots"><i></i><i></i><i class="on"></i><i></i><i></i><i></i></div>
  </div>

  <h2 class="abs h-under welcome">Welcome To Our Show</h2>
  <div class="abs intro">
    <p>Lorem ipsum dolor sit amet, consectetur adipisicing elit, sed do eiusmod tempor incididunt ut labore et dolore magna aliqua. Ut enim ad minim veniam.Lorem ipsum dolor sit amet, consectetur adipisicing elit, sed do eiusmod tempor incididunt ut labore et dolore magna aliqua. Ut enim ad minim veniam.</p>
    <p>Lorem ipsum dolor sit amet, consectetur adipisicing elit, sed do eiusmod tempor incididunt ut labore et dolore magna aliqua. Ut enim ad minim veniam.</p>
    <p>Lorem ipsum dolor sit amet, consectetur adipisicing elit, sed do eiusmod tempor incididunt ut labore et dolore magna aliqua. Ut enim ad minim veniam.Lorem ipsum dolor sit amet, consectetur adipisicing elit, sed do eiusmod tempor incididunt ut labore et dolore magna aliqua. Ut enim ad minim veniam.</p>
  </div>

  <section class="abs panel">
    <div class="abs barhead" style="left:10px;top:14px;width:549px"><h3>PAST SHOWS</h3><a>See all Past Shows</a></div>

    <article class="abs card" style="left:10px;top:50px">
      <div class="photo warm" role="img" aria-label="Host at a cluttered studio desk"></div>
      <h4>Lorem ipsum dolor sit amet,</h4>
      <div class="meta"><div class="date">JAN 5,2014</div>Author : John Joe<br>Website : <a>www.authorsite.example</a></div>
      <p class="desc">Lorem ipsum dolor sit amet, consectetur adipisicing elit, sed do eiusmod tempor incididunt ut labore et dolore magna aliqua. Ut enim ad minim veniam. <span class="more">More...</span></p>
    </article>
    <article class="abs card" style="left:199px;top:50px">
      <div class="photo cool" role="img" aria-label="Guest wearing headphones at the microphone"></div>
      <h4>Lorem ipsum dolor sit amet,</h4>
      <div class="meta"><div class="date">JAN 5,2014</div>Author : John Joe<br>Website : <a>www.authorsite.example</a></div>
      <p class="desc">Lorem ipsum dolor sit amet, consectetur adipisicing elit, sed do eiusmod tempor incididunt ut labore et dolore magna aliqua. Ut enim ad minim veniam. <span class="more">More...</span></p>
    </article>
    <article class="abs card" style="left:388px;top:50px">
      <div class="photo room" role="img" aria-label="Three guests around a studio table"></div>
      <h4>Lorem ipsum dolor sit amet,</h4>
      <div class="meta"><div class="date">JAN 5,2014</div>Author : John Joe<br>Website : <a>www.authorsite.example</a></div>
      <p class="desc">Lorem ipsum dolor sit amet, consectetur adipisicing elit, sed do eiusmod tempor incididunt ut labore et dolore magna aliqua. Ut enim ad minim veniam. <span class="more">More...</span></p>
    </article>

    <div class="abs barhead" style="left:10px;top:285px;width:372px"><h3>UPCOMING SHOWS</h3><a>See all Upcoming Shows</a></div>
    <div class="abs thumb" style="left:11px;top:313px">
      <div class="photo warm" role="img" aria-label="Host at a studio desk"></div>
      <p>Lorem ipsum dolor sit amet,sed do eiusmod tempor incididunt ut</p><small>MAR 5,2014</small>
    </div>
    <div class="abs thumb" style="left:138px;top:313px">
      <div class="photo room" role="img" aria-label="Guests seated in the studio"></div>
      <p>Lorem ipsum dolor sit amet,sed do eiusmod tempor incididunt ut</p><small>MAR 5,2014</small>
    </div>
    <div class="abs thumb" style="left:264px;top:313px">
      <div class="photo warm" role="img" aria-label="Two guests talking at microphones"></div>
      <p>Lorem ipsum dolor sit amet,sed do eiusmod tempor incididunt ut</p><small>MAR 5,2014</small>
    </div>

    <div class="abs videobox">
      <h2 class="h-under">Latest Video</h2>
      <div class="photo room" role="img" aria-label="Band performing in the studio">
        <svg class="abs" style="left:57px;top:24px" width="30" height="30" viewBox="0 0 30 30"><circle cx="15" cy="15" r="13" fill="rgba(255,255,255,.35)" stroke="rgba(255,255,255,.8)" stroke-width="2"/><path d="M12 9l9 6-9 6z" fill="rgba(255,255,255,.85)"/></svg>
      </div>
    </div>
  </section>

  <section class="abs col" style="left:7px;width:170px">
    <h2 class="h-under" style="width:49px">Blog</h2>
    <div class="list-item">Lorem ipsum dolor sit amet, consectetur adipisicing elit, sed do eiusmod tempor incididunt ut labore et dolore magna aliqua. Ut enim ad minim veniam,<span class="date">JAN 4,2014</span></div>
    <div class="list-item">Lorem ipsum dolor sit amet, consectetur adipisicing elit, sed do eiusmod tempor incididunt ut labore et dolore magna aliqua. Ut enim ad minim veniam,<span class="date">JAN 4,2014</span></div>
    <div class="list-item">Lorem ipsum dolor sit amet, consectetur adipisicing elit, sed do eiusmod tempor incididunt ut labore et dolore magna aliqua. Ut enim ad minim veniam,<span class="date">JAN 4,2014</span></div>
  </section>

  <section class="abs col" style="left:199px;width:175px">
    <h2 class="h-under" style="width:49px">Chirps</h2>
    <div class="chirp first"><span class="dot"></span><div>Lorem ipsum dolor sit amet, consectetur adipisicing elit, sed do eiusmod tempor incididunt ut labore et<span class="date">JAN 4,2014</span></div></div>
    <div class="chirp"><span class="dot"></span><div>Lorem ipsum dolor sit amet, consectetur adipisicing elit, sed do eiusmod tempor incididunt ut labore et<span class="date">JAN 4,2014</span></div></div>
    <div class="chirp"><span class="dot"></span><div>Lorem ipsum dolor sit amet, consectetur adipisicing elit, sed do eiusmod tempor incididunt ut labore et<span class="date">JAN 4,2014</span></div></div>
    <div class="chirp"><span class="dot"></span><div>Lorem ipsum dolor sit amet, consectetur adipisicing elit, sed do eiusmod tempor incididunt ut labore et<span class="date">JAN 4,2014</span></div></div>
  </section>

  <aside class="abs playlist">
    <header>FEATURED PLAYLIST</header>
    <div class="track"><h5>WHY VINYL SOUNDS BETTER THAN CD, OR NOT</h5><p>Two experts explain the audio science behind the music. <span class="play">Play</span></p></div>
    <div class="track"><h5>WHY VINYL SOUNDS BETTER THAN CD, OR NOT</h5><p>Two experts explain the audio science behind the music. <span class="play">Play</span></p></div>
    <div class="track"><h5>WHY VINYL SOUNDS BETTER THAN CD, OR NOT</h5><p>Two experts explain the audio science behind the music. <span class="play">Play</span></p></div>
    <div class="more-list">More Playlist</div>
  </aside>

  <footer class="abs footer">
    <div class="abs foot-links"><span>Sitemap</span><span>Newsletter</span><span>Blog</span><span>Contact Us</span><span>Privacy&amp;policy</span></div>
    <div class="abs copy">Copyrights@2014.All Right Reserved</div>
    <div class="abs foot-brand"><span class="sq"></span>VandorFM</div>
  </footer>
</div>
</body>
</html>
```